Business Card Design Project

looking for business cards with new logo

I am looking to keep with the colors of the logo i posted.  Here are some other details to consider.  I would like my website prominently displayed on the business card with the logo.  my website is www.HavenrockTX.com...it should be spelled this way.

My contact information is:

Daniel P Whitcomb III
Broker/Owner
48391 Cordell Ave., Suite 307
Helotes, Texas 78023
Office: 210-555-0147
Email:  Daniel@HavenrockTX.com

Thank you
Daniel Whitcomb

```html
<!DOCTYPE html>
<html lang="en">
<head>
<meta charset="utf-8">
<title>Havenrock Realty – Business Cards</title>
<link rel="stylesheet" href="https://fonts.googleapis.com/css2?family=Open+Sans:wght@400;600;700&display=swap">
<style>
  :root {
    --ink: #050505;
    --sky: #3fbdf0;
    --sky-deep: #0b7fc4;
    --sky-soft: #6fd0f5;
    --white: #ffffff;
    --page: #e9ecea;
    --text-dark: #10222c;
  }
  * { margin: 0; padding: 0; box-sizing: border-box; }
  html, body { width: 1080px; height: 1200px; overflow: hidden; }
  body {
    background: var(--page);
    font-family: "Open Sans", Arial, sans-serif;
    position: relative;
  }
  .card {
    position: absolute;
    left: 90px;
    width: 900px;
    height: 514px;
    background: var(--ink);
    overflow: hidden;
    box-shadow: 0 10px 30px rgba(0,0,0,0.25);
  }
  .card--front { top: 57px; }
  .card--back { top: 628px; }

  .lockup {
    position: absolute;
    display: flex;
    flex-direction: column;
    white-space: nowrap;
  }
  .brand {
    display: flex;
    align-items: center;
    gap: 18px;
    color: var(--white);
    font-weight: 600;
  }
  .brand__mark { background: var(--sky); flex: none; }
  .website {
    color: var(--sky);
    font-weight: 600;
    letter-spacing: 1px;
  }

  .card--front .lockup {
    left: 0; right: 0; top: 0; bottom: 0;
    align-items: center;
    justify-content: center;
    gap: 22px;
  }
  .card--front .brand { font-size: 64px; letter-spacing: 1px; }
  .card--front .brand__mark { width: 46px; height: 46px; }
  .card--front .website { font-size: 30px; }

  .card--back .lockup {
    left: 48px; top: 262px;
    gap: 10px;
  }
  .card--back .brand { font-size: 40px; }
  .card--back .brand__mark { width: 30px; height: 30px; }
  .card--back .website { font-size: 22px; padding-left: 48px; }

  .top-band {
    position: absolute;
    left: 0; top: 0; width: 100%; height: 66px;
    background: var(--sky);
    border-bottom: 6px solid var(--ink);
  }
  .holder {
    position: absolute;
    right: 24px; top: 8px;
    text-align: right;
  }
  .holder__name {
    color: var(--sky-deep);
    font-weight: 700;
    font-size: 25px;
    line-height: 1.1;
  }
  .holder__title {
    color: var(--ink);
    font-weight: 700;
    font-size: 13px;
    line-height: 1.2;
  }
  .contact-box {
    position: absolute;
    left: 468px; top: 108px;
    width: 410px; height: 220px;
    background: linear-gradient(135deg, var(--sky-soft) 0%, var(--sky) 55%, #1aa6e2 100%);
    padding: 62px 26px 0 28px;
    color: var(--text-dark);
    font-size: 19px;
    line-height: 1.42;
  }
  .stripes {
    position: absolute;
    left: 0; bottom: 0; width: 100%; height: 118px;
  }
</style>
</head>
<body>
  <section class="card card--front" aria-label="Front of business card">
    <div class="lockup">
      <div class="brand"><span class="brand__mark"></span><span class="brand__name">Havenrock Realty</span></div>
      <p class="website">www.HavenrockTX.com</p>
    </div>
  </section>

  <section class="card card--back" aria-label="Back of business card">
    <header class="top-band">
      <div class="holder">
        <p class="holder__name">Daniel P Whitcomb III</p>
        <p class="holder__title">Broker/Owner</p>
      </div>
    </header>

    <div class="contact-box">
      <p>48391 Cordell Ave., Suite 307</p>
      <p>Helotes, Texas 78023</p>
      <p>Office: 210-555-0147</p>
      <p>Email:&nbsp; Daniel@HavenrockTX.com</p>
    </div>

    <div class="lockup">
      <div class="brand"><span class="brand__mark"></span><span class="brand__name">Havenrock Realty</span></div>
      <p class="website">www.HavenrockTX.com</p>
    </div>

    <svg class="stripes" viewBox="0 0 900 118" preserveAspectRatio="none" aria-hidden="true">
      <rect x="0" y="0" width="900" height="118" fill="var(--sky)"/>
      <rect x="0" y="0" width="900" height="26" fill="var(--ink)"/>
      <rect x="0" y="44" width="900" height="8" fill="var(--ink)"/>
      <rect x="0" y="68" width="900" height="6" fill="var(--ink)"/>
      <rect x="0" y="88" width="900" height="5" fill="var(--ink)"/>
      <rect x="0" y="104" width="900" height="4" fill="var(--ink)"/>
    </svg>
  </section>
</body>
</html>
```